Brackwell Engineering Inc. Marketing Brochure

need a brochure designed for Brackwell Engineering Inc. It would follow the theme of www.brackwelleng.ca. It would be ~7" x 9" in size. Full Color. 4 pages. Please refer to BrackwellENG.ca to get the description of our services. The text font will be in the attached documents also. The theme must be industrial but also smart telling the customer that we use the latest in 3d cadworx to build our facilities. https://www.lookvarne.ca/find?q=3d+cadworx+images&type=img&src=qx&ctx=1&ref=MqTrodLP48vnzaX%253A%252C_2p9HbeW_4kjsT%252C_&tok=ZkwpRmq83LuxnVD-KolQW71-h3pjk_PRat&sa=Y&vid=9bhPRmxTy4kLmWf8KbQn1jLqPwRtsYcVb4HkTzXqW2pDcGhWqY#imgid=RK8M_4x2pzqm7N:&imgref=MqTrodLP48vnzaX:

Industry/Entity Type

Oil And Gas Exploration

Requirements
Must have
• a 7" x 9" brochure that is snappy, smart and crisp along the same lines at the brackwelleng.ca website.
Nice to have
• it must include the "services" listed on the brackwelleng.ca website
• It must really highlight the brand of name Brackwell Engineering Inc. AND the polar bear.
• Mission Statement: Brackwell Engineering Inc. offers fit-for-purpose, pragmatic EPCM (Engineering, Procurement and Construction Management) and Asset Management Consulting (MOC) in a timely, cost effective manner built on the foundations of safety, environmental protection and cost control.
Should not have
• it must not be too overly "wordy". We are selling an IMAGE and a BRAND here more than anything.
• Remove/do not include the Brackwell Engineering is Back paragraph... I want to move my messaging away from that theme.

```html
<!DOCTYPE html>
<html lang="en">
<head>
<meta charset="utf-8">
<title>Brackwell Engineering Inc. Brochure</title>
<link href="https://fonts.googleapis.com/css2?family=Montserrat:wght@500;600;700;800&family=Open+Sans:wght@400;600;700&display=swap" rel="stylesheet">
<style>
  :root{
    --stage:#4b4b4e;
    --cover-grey:#a7a9b1;
    --cover-grey-light:#c9cbd2;
    --navy:#1f2a78;
    --navy-deep:#161d5a;
    --accent:#2f8fe0;
    --ink:#1c1d22;
    --white:#ffffff;
    --charcoal:#28292d;
    --charcoal-light:#3b3c42;
    --body-grey:#9a9ca3;
  }
  *{box-sizing:border-box;margin:0;padding:0}
  html,body{width:906px;height:1200px;overflow:hidden}
  body{background:var(--stage);font-family:"Montserrat",sans-serif;position:relative}

  .spread{position:absolute;left:43px;width:820px;height:527px;overflow:hidden;box-shadow:0 10px 30px rgba(0,0,0,.35)}
  .spread--cover{top:40px}
  .spread--inside{top:633px;background:var(--charcoal)}
  .spread__art{position:absolute;inset:0;width:100%;height:100%}
  .spread__fold{position:absolute;left:409px;top:0;width:2px;height:100%;background:rgba(0,0,0,.18)}

  /* cover */
  .contact{position:absolute;left:40px;top:92px;color:var(--white)}
  .contact__title{font-size:17px;font-weight:700;letter-spacing:.2px}
  .contact__rule{width:60px;height:2px;background:var(--accent);margin:6px 0 12px}
  .contact__list{list-style:none;position:relative;padding-left:20px}
  .contact__list::before{content:"";position:absolute;left:4px;top:7px;bottom:7px;width:1.5px;background:var(--accent)}
  .contact__item{font-size:12.5px;font-weight:600;line-height:22px;position:relative}
  .contact__item::before{content:"";position:absolute;left:-20px;top:7px;width:9px;height:9px;border-radius:50%;border:2px solid var(--accent);background:var(--navy-deep)}

  .partners{position:absolute;left:40px;top:400px;color:var(--ink)}
  .partners__label{font-size:12px;font-weight:600;margin-bottom:5px}
  .partners__name{display:flex;align-items:center;gap:7px;font-size:17px;font-weight:700;color:var(--navy);margin-bottom:12px}
  .partners__mark{width:14px;height:14px;background:var(--navy)}
  .partners__mark--round{border-radius:50%}

  .brand{position:absolute;left:590px;top:34px;display:flex;align-items:center;gap:10px;color:var(--ink)}
  .brand__mark{width:34px;height:34px;border-radius:50%;background:var(--accent)}
  .brand__name{font-size:15px;font-weight:800;line-height:15px;text-transform:uppercase}

  /* inside */
  .section-title{position:absolute;left:40px;top:52px;font-size:23px;font-weight:700;color:var(--accent)}
  .services{position:absolute;font-family:"Open Sans",sans-serif;color:var(--white)}
  .services--left{left:40px;top:132px;width:340px}
  .services--right{left:446px;top:44px;width:340px}
  .services__heading{font-size:13px;font-weight:700;display:inline-block;border-bottom:2px solid var(--accent);padding-bottom:1px;margin-bottom:8px}
  .services__heading--gap{margin-top:8px}
  .service{position:relative;padding-left:16px;margin-bottom:8px}
  .service__icon{position:absolute;left:0;top:2px;width:10px;height:10px}
  .service__name{font-size:9.5px;font-weight:600;color:var(--accent);line-height:12px}
  .service__text{font-size:7.2px;line-height:9.5px;color:var(--body-grey)}
</style>
</head>
<body>

<!-- Cover spread: back cover (left) and front cover (right) -->
<section class="spread spread--cover">
  <svg class="spread__art" viewBox="0 0 820 527" preserveAspectRatio="none">
    <defs>
      <linearGradient id="coverGrey" x1="0" y1="0" x2="1" y2="1">
        <stop offset="0" stop-color="#c9cbd2"/>
        <stop offset="1" stop-color="#9ea0a8"/>
      </linearGradient>
      <linearGradient id="refinerySky" x1="0" y1="0" x2="0" y2="1">
        <stop offset="0" stop-color="#3b3f8f"/>
        <stop offset=".38" stop-color="#8d78a8"/>
        <stop offset=".55" stop-color="#e2b08a"/>
        <stop offset=".72" stop-color="#6a6c86"/>
        <stop offset="1" stop-color="#1d2540"/>
      </linearGradient>
      <linearGradient id="navyVeil" x1="0" y1="0" x2="1" y2="0">
        <stop offset="0" stop-color="#1a2170" stop-opacity=".97"/>
        <stop offset=".6" stop-color="#2a3390" stop-opacity=".85"/>
        <stop offset="1" stop-color="#2a3390" stop-opacity="0"/>
      </linearGradient>
    </defs>
    <rect width="820" height="527" fill="url(#coverGrey)"/>
    <polygon points="0,0 410,0 820,300 820,527 410,527 0,330" fill="url(#refinerySky)" role="img" aria-label="Photo of an oil refinery at dusk under a purple and orange sky"/>
    <polygon points="0,0 410,0 560,110 410,527 0,330" fill="url(#navyVeil)"/>
    <line x1="440" y1="10" x2="760" y2="245" stroke="#ffffff" stroke-width="7" stroke-linecap="round" opacity=".9"/>
    <line x1="560" y1="60" x2="800" y2="236" stroke="#4a4b52" stroke-width="9" stroke-linecap="round"/>
    <line x1="30" y1="310" x2="370" y2="488" stroke="#ffffff" stroke-width="7" stroke-linecap="round" opacity=".9"/>
    <line x1="90" y1="360" x2="400" y2="520" stroke="#4a4b52" stroke-width="9" stroke-linecap="round"/>
  </svg>
  <div class="spread__fold"></div>

  <div class="contact">
    <p class="contact__title">Call Us for Free consultation now</p>
    <div class="contact__rule"></div>
    <ul class="contact__list">
      <li class="contact__item">(555) 014-2290</li>
      <li class="contact__item">contactus@brackwelleng.ca</li>
      <li class="contact__item">www.brackwelleng.ca</li>
    </ul>
  </div>

  <div class="partners">
    <p class="partners__label">Project Control</p>
    <p class="partners__name"><span class="partners__mark partners__mark--round"></span>LedgerPoint</p>
    <p class="partners__label">Asset Management (M.O.C)</p>
    <p class="partners__name"><span class="partners__mark"></span>ChangeWell</p>
  </div>

  <div class="brand">
    <span class="brand__mark"></span>
    <p class="brand__name">Brackwell<br>Engineering<br>Inc</p>
  </div>
</section>

<!-- Inside spread: services -->
<section class="spread spread--inside">
  <svg class="spread__art" viewBox="0 0 820 527" preserveAspectRatio="none">
    <defs>
      <linearGradient id="insideBg" x1="0" y1="0" x2="1" y2="1">
        <stop offset="0" stop-color="#2b2c31"/>
        <stop offset="1" stop-color="#3d3e44"/>
      </linearGradient>
      <linearGradient id="cornerGrey" x1="0" y1="0" x2="1" y2="1">
        <stop offset="0" stop-color="#d2d4da"/>
        <stop offset="1" stop-color="#9a9ca4"/>
      </linearGradient>
      <linearGradient id="siteWarm" x1="0" y1="0" x2="1" y2="1">
        <stop offset="0" stop-color="#c89a4a"/>
        <stop offset=".5" stop-color="#7a5a2e"/>
        <stop offset="1" stop-color="#2e2a26"/>
      </linearGradient>
      <linearGradient id="plantBlue" x1="0" y1="0" x2="1" y2="0">
        <stop offset="0" stop-color="#1f4fa8"/>
        <stop offset=".45" stop-color="#3a6fc0"/>
        <stop offset="1" stop-color="#b9bfc9"/>
      </linearGradient>
      <radialGradient id="figureShade" cx=".5" cy=".5" r=".5">
        <stop offset="0" stop-color="#1c1d21" stop-opacity=".7"/>
        <stop offset="1" stop-color="#1c1d21" stop-opacity="0"/>
      </radialGradient>
    </defs>
    <rect width="820" height="527" fill="url(#insideBg)"/>
    <ellipse cx="420" cy="260" rx="190" ry="220" fill="url(#figureShade)" role="img" aria-label="Faint silhouette of an engineer in a hard hat"/>
    <path d="M0 0 H300 Q150 60 0 175 Z" fill="url(#cornerGrey)"/>
    <polygon points="205,0 410,0 410,92 300,122 190,52" fill="url(#siteWarm)" role="img" aria-label="Photo of heavy equipment and refinery stacks at sunset"/>
    <path d="M820 300 Q690 430 590 527 H820 Z" fill="url(#cornerGrey)"/>
    <polygon points="410,527 410,445 520,410 640,448 600,527" fill="url(#plantBlue)" role="img" aria-label="Photo of a welder inside a pipe and a 3D plant model"/>
  </svg>
  <div class="spread__fold"></div>

  <h2 class="section-title">Our Services</h2>

  <div class="services services--left">
    <h3 class="services__heading">EPCM</h3>
    <div class="service"><svg class="service__icon" viewBox="0 0 10 10"><path d="M1 9 L7 3 M5 1 L9 5" stroke="#cfd1d6" stroke-width="1.8" stroke-linecap="round"/></svg><p class="service__name">Oil &amp; Gas Pipelines</p><p class="service__text">Lorem Ipsum is simply dummy text of the printing and typesetting industry. when an unknown printer took a galley of type and scrambled it to make a type specimen book.</p></div>
    <div class="service"><svg class="service__icon" viewBox="0 0 10 10"><path d="M1 9 L7 3 M5 1 L9 5" stroke="#cfd1d6" stroke-width="1.8" stroke-linecap="round"/></svg><p class="service__name">Debottlenecking</p><p class="service__text">Lorem Ipsum is simply dummy text of the printing and typesetting industry. when an unknown printer took a galley of type and scrambled it to make a type specimen book.</p></div>
    <div class="service"><svg class="service__icon" viewBox="0 0 10 10"><path d="M1 9 L7 3 M5 1 L9 5" stroke="#cfd1d6" stroke-width="1.8" stroke-linecap="round"/></svg><p class="service__name">Compression</p><p class="service__text">Lorem Ipsum is simply dummy text of the printing and typesetting industry. when an unknown printer took a galley of type and scrambled it to make a type specimen book.</p></div>
    <div class="service"><svg class="service__icon" viewBox="0 0 10 10"><path d="M1 9 L7 3 M5 1 L9 5" stroke="#cfd1d6" stroke-width="1.8" stroke-linecap="round"/></svg><p class="service__name">Refrigeration</p><p class="service__text">Lorem Ipsum is simply dummy text of the printing and typesetting industry. when an unknown printer took a galley of type and scrambled it to make a type specimen book.</p></div>
    <div class="service"><svg class="service__icon" viewBox="0 0 10 10"><path d="M1 9 L7 3 M5 1 L9 5" stroke="#cfd1d6" stroke-width="1.8" stroke-linecap="round"/></svg><p class="service__name">Oil Batteries</p><p class="service__text">Lorem Ipsum is simply dummy text of the printing and typesetting industry. when an unknown printer took a galley of type and scrambled it to make a type specimen book.</p></div>
    <div class="service"><svg class="service__icon" viewBox="0 0 10 10"><path d="M1 9 L7 3 M5 1 L9 5" stroke="#cfd1d6" stroke-width="1.8" stroke-linecap="round"/></svg><p class="service__name">Hazops</p><p class="service__text">Lorem Ipsum is simply dummy text of the printing and typesetting industry. when an unknown printer took a galley of type and scrambled it to make a type specimen book.</p></div>
    <div class="service"><svg class="service__icon" viewBox="0 0 10 10"><path d="M1 9 L7 3 M5 1 L9 5" stroke="#cfd1d6" stroke-width="1.8" stroke-linecap="round"/></svg><p class="service__name">Process Reviews and capacity studies</p><p class="service__text">Lorem Ipsum is simply dummy text of the printing and typesetting industry. when an unknown printer took a galley of type and scrambled it to make a type specimen book.</p></div>
  </div>

  <div class="services services--right">
    <h3 class="services__heading">Asset Management</h3>
    <div class="service"><svg class="service__icon" viewBox="0 0 10 10"><path d="M1 9 L7 3 M5 1 L9 5" stroke="#cfd1d6" stroke-width="1.8" stroke-linecap="round"/></svg><p class="service__name">EPAP Programs</p><p class="service__text">Lorem Ipsum is simply dummy text of the printing and typesetting industry. when an unknown printer took a galley of type and scrambled it to make a type specimen book.</p></div>
    <div class="service"><svg class="service__icon" viewBox="0 0 10 10"><path d="M1 9 L7 3 M5 1 L9 5" stroke="#cfd1d6" stroke-width="1.8" stroke-linecap="round"/></svg><p class="service__name">Maintenance Management</p><p class="service__text">Lorem Ipsum is simply dummy text of the printing and typesetting industry. when an unknown printer took a galley of type and scrambled it to make a type specimen book.</p></div>
    <div class="service"><svg class="service__icon" viewBox="0 0 10 10"><path d="M1 9 L7 3 M5 1 L9 5" stroke="#cfd1d6" stroke-width="1.8" stroke-linecap="round"/></svg><p class="service__name">Integrity Management</p><p class="service__text">Lorem Ipsum is simply dummy text of the printing and typesetting industry. when an unknown printer took a galley of type and scrambled it to make a type specimen book.</p></div>
    <h3 class="services__heading services__heading--gap">Exploitation</h3>
    <div class="service"><svg class="service__icon" viewBox="0 0 10 10"><path d="M1 9 L7 3 M5 1 L9 5" stroke="#cfd1d6" stroke-width="1.8" stroke-linecap="round"/></svg><p class="service__name">Type Curve Development</p><p class="service__text">Lorem Ipsum is simply dummy text of the printing and typesetting industry. when an unknown printer took a galley of type and scrambled it to make a type specimen book.</p></div>
    <div class="service"><svg class="service__icon" viewBox="0 0 10 10"><path d="M1 9 L7 3 M5 1 L9 5" stroke="#cfd1d6" stroke-width="1.8" stroke-linecap="round"/></svg><p class="service__name">A &amp; D</p><p class="service__text">Lorem Ipsum is simply dummy text of the printing and typesetting industry. when an unknown printer took a galley of type and scrambled it to make a type specimen book.</p></div>
    <div class="service"><svg class="service__icon" viewBox="0 0 10 10"><path d="M1 9 L7 3 M5 1 L9 5" stroke="#cfd1d6" stroke-width="1.8" stroke-linecap="round"/></svg><p class="service__name">ValTrek modeling</p><p class="service__text">Lorem Ipsum is simply dummy text of the printing and typesetting industry. when an unknown printer took a galley of type and scrambled it to make a type specimen book.</p></div>
    <div class="service"><svg class="service__icon" viewBox="0 0 10 10"><path d="M1 9 L7 3 M5 1 L9 5" stroke="#cfd1d6" stroke-width="1.8" stroke-linecap="round"/></svg><p class="service__name">Development planning</p><p class="service__text">Lorem Ipsum is simply dummy text of the printing and typesetting industry. when an unknown printer took a galley of type and scrambled it to make a type specimen book.</p></div>
  </div>
</section>

</body>
</html>
```